Copperfield Ridge Dental business card

Business card would have following info:

Harold T. Quenneville, DMD, FAGD
General Dentist
email: office@copperfieldridgedental.com
phone: 413-867-3094
fax: 413-867-3094
website: copperfieldridgedental.com

second side would have lines for:

appointment date
appointment time

```html
<!DOCTYPE html>
<html lang="en">
<head>
<meta charset="utf-8">
<title>Copperfield Ridge Dental – Business Card</title>
<link href="https://fonts.googleapis.com/css2?family=Lato:wght@400;700;900&display=swap" rel="stylesheet">
<style>
  :root{
    --purple:#6f3d98;
    --purple-deep:#5e2e8a;
    --orange:#f39222;
    --white:#ffffff;
    --ink:#1d1d1f;
    --backdrop:#2b2b2d;
  }
  *{box-sizing:border-box;margin:0;padding:0}
  html,body{width:1200px;height:875px;overflow:hidden}
  body{background:var(--backdrop);font-family:"Lato",sans-serif;position:relative}

  .card{position:absolute;top:279px;width:555px;height:317px;background:var(--white);border-radius:20px;overflow:hidden}
  .card--appointment{left:30px}
  .card--contact{left:615px}

  /* appointment side */
  .appt-title{position:absolute;top:40px;left:0;width:100%;text-align:center;color:var(--purple);font-weight:900;font-size:31px;letter-spacing:.5px}
  .field-row{position:absolute;left:44px;right:44px;display:flex;align-items:flex-end;font-size:14px;color:var(--ink);text-transform:uppercase}
  .field-row--name{top:112px}
  .field-row--date{top:150px}
  .field-line{flex:1;border-bottom:1.5px dotted #555;margin:0 4px 3px;height:1px}
  .field-suffix{font-size:11px}
  .days{position:absolute;top:200px;left:44px;right:44px;display:flex;justify-content:space-between;font-size:15px;color:var(--ink)}
  .day{display:flex;align-items:center;gap:6px}
  .day-box{width:13px;height:13px;border:2px solid var(--orange)}
  .appt-note{position:absolute;top:250px;left:70px;right:70px;text-align:center;font-size:11.5px;line-height:1.4;color:var(--ink)}

  /* contact side */
  .wave{position:absolute;inset:0;width:555px;height:317px}
  .practice-name{position:absolute;top:58px;left:42px;color:var(--purple);font-weight:900;font-size:30px;line-height:1.05;letter-spacing:.5px;text-transform:uppercase}
  .practice-name .practice-sub{display:block;font-size:17px;letter-spacing:11px;margin-top:6px;padding-left:40px}
  .dentist{position:absolute;left:28px;top:226px;width:250px;text-align:right}
  .dentist-name{color:var(--orange);font-weight:900;font-size:19px;text-transform:uppercase;letter-spacing:.3px;white-space:nowrap}
  .dentist-cred{color:var(--orange);font-size:15px;margin-top:2px}
  .dentist-role{color:var(--white);font-size:15px}
  .divider{position:absolute;left:292px;top:220px;width:1.5px;height:82px;background:var(--orange)}
  .contact-list{position:absolute;left:306px;top:218px;list-style:none;color:var(--white);font-size:12.5px;line-height:21px}
  .contact-list li{display:flex;align-items:center;gap:8px;white-space:nowrap}
  .contact-list svg{width:11px;height:11px;flex:none}
</style>
</head>
<body>

<section class="card card--appointment" aria-label="Next appointment card">
  <h1 class="appt-title">NEXT APPOINTMENT</h1>
  <div class="field-row field-row--name"><span>Name</span><span class="field-line"></span></div>
  <div class="field-row field-row--date"><span>Date</span><span class="field-line"></span><span>Time</span><span class="field-line"></span><span class="field-suffix">AM\PM</span></div>
  <div class="days">
    <span class="day"><span class="day-box"></span>MON</span>
    <span class="day"><span class="day-box"></span>TUES</span>
    <span class="day"><span class="day-box"></span>WED</span>
    <span class="day"><span class="day-box"></span>THU</span>
    <span class="day"><span class="day-box"></span>FRI</span>
    <span class="day"><span class="day-box"></span>SAT</span>
  </div>
  <p class="appt-note">If you are unable to keep your appointment, please call us to reschedule at least 48 hours prior to your appointment.</p>
</section>

<section class="card card--contact" aria-label="Contact card">
  <svg class="wave" viewBox="0 0 555 317" aria-hidden="true">
    <path d="M0,244 C170,222 330,196 420,112 C465,72 505,52 555,44 L555,317 L0,317 Z" fill="var(--purple)"/>
    <path d="M0,226 C160,210 300,190 380,130 C330,172 180,206 0,218 Z" fill="var(--purple)"/>
    <path d="M250,214 C350,180 400,120 455,70 C490,42 520,30 555,22 L555,28 C520,38 492,52 462,80 C410,130 360,185 250,214 Z" fill="var(--orange)"/>
  </svg>

  <div class="practice-name">Copperfield Ridge<span class="practice-sub">Dental</span></div>

  <div class="dentist">
    <div class="dentist-name">Harold T. Quenneville</div>
    <div class="dentist-cred">DMD, FAGD</div>
    <div class="dentist-role">General Dentist</div>
  </div>

  <div class="divider"></div>

  <ul class="contact-list">
    <li><svg viewBox="0 0 24 24"><path fill="var(--orange)" d="M6.6 10.8a15 15 0 006.6 6.6l2.2-2.2a1 1 0 011-.25 11.4 11.4 0 003.6.57 1 1 0 011 1V20a1 1 0 01-1 1A17 17 0 013 4a1 1 0 011-1h3.5a1 1 0 011 1 11.4 11.4 0 00.57 3.6 1 1 0 01-.25 1z"/></svg>413-867-3094</li>
    <li><svg viewBox="0 0 24 24"><path fill="var(--orange)" d="M6 2h10l2 2v5H6zM3 10h18v9h-3v3H6v-3H3zm5 6v4h8v-4z"/></svg>413-867-3094</li>
    <li><svg viewBox="0 0 24 24"><path fill="var(--orange)" d="M2 5h20v14H2zm2 2v.5l8 5 8-5V7l-8 5z"/></svg>office@copperfieldridgedental.com</li>
    <li><svg viewBox="0 0 24 24"><circle cx="12" cy="12" r="9" fill="none" stroke="var(--orange)" stroke-width="2.5"/><path d="M3 12h18M12 3c4 4 4 14 0 18M12 3c-4 4-4 14 0 18" fill="none" stroke="var(--orange)" stroke-width="2"/></svg>copperfieldridgedental.com</li>
  </ul>
</section>

</body>
</html>
```